Banner Design for Websites

I am looking for a few various banner designs of the below size. I want them to look authentic, bold and catchy.
Width 939
Height 262
Wording:
WANTED: DRIVEN AND SUCCESSFUL INDIVIDUALS READY TO TAKE THEIR RESULTS TO THE NEXT LEVEL.

Make up to $5000 per sale
No cold calling
No experience required
No pressure selling
NOT MLM

Personal Empowerment. The Next Big Business Boom !

I make well in excess of 10k per month consistently. Marnie K

Some photos attached for use and also some others banners for various workding other than above.

```html
<!DOCTYPE html>
<html lang="en">
<head>
<meta charset="utf-8">
<title>Personal Empowerment Banner</title>
<link rel="stylesheet" href="https://fonts.googleapis.com/css2?family=Stardos+Stencil:wght@700&family=Russo+One&family=Arimo:ital,wght@1,700&display=swap">
<style>
  :root {
    --page: #ffffff;
    --wanted-yellow: #fff200;
    --white: #ffffff;
    --ink: #0a0a0a;
    --rose-top: #c75470;
    --rose-mid: #a52a45;
    --wine: #6e0716;
    --wine-deep: #560010;
    --photo-dark: #2b1a16;
    --photo-warm: #6b4530;
  }
  * { margin: 0; padding: 0; box-sizing: border-box; }
  html, body {
    width: 1200px; height: 697px; overflow: hidden;
    background: var(--page);
  }
  .stage {
    position: relative; width: 1200px; height: 697px;
  }
  .banner {
    position: absolute;
    left: 36px; top: 191px;
    width: 939px; height: 262px;
    transform: scale(1.2);
    transform-origin: 0 0;
    overflow: hidden;
  }
  .banner-shapes {
    position: absolute; inset: 0; width: 939px; height: 262px;
  }
  .photo-slot {
    position: absolute; left: 742px; top: 0; width: 197px; height: 262px;
    background: linear-gradient(90deg, rgba(43,26,22,0) 0%, var(--photo-dark) 14%, var(--photo-warm) 60%, var(--photo-dark) 100%);
  }
  .headline-wanted {
    position: absolute; left: 0; top: 14px; width: 344px;
    text-align: center;
    font-family: "Stardos Stencil", "Impact", sans-serif;
    font-weight: 700; font-size: 74px; line-height: 1;
    color: var(--wanted-yellow);
    letter-spacing: 1px;
  }
  .headline-call {
    position: absolute; left: 0; top: 104px; width: 346px;
    text-align: center;
    font-family: "Russo One", "Arial Black", sans-serif;
    font-size: 24.5px; line-height: 36px;
    color: var(--white);
    letter-spacing: 0.6px;
  }
  .offer-title {
    position: absolute; left: 355px; top: 15px; width: 400px;
    text-align: center;
    font-family: "Arimo", "Arial", sans-serif;
    font-style: italic; font-weight: 700;
    font-size: 22px; line-height: 1.2;
    color: var(--white);
  }
  .offer-subtitle {
    position: absolute; left: 345px; top: 49px; width: 400px;
    text-align: center;
    font-family: "Arimo", "Arial", sans-serif;
    font-style: italic; font-weight: 700;
    font-size: 22.5px; line-height: 1.2;
    color: var(--ink);
  }
  .benefit-list {
    position: absolute; left: 0; top: 85px;
    list-style: none;
    font-family: "Arimo", "Arial", sans-serif;
    font-style: italic; font-weight: 700;
    font-size: 17px; line-height: 21.8px;
    color: var(--wanted-yellow);
  }
  .benefit-list li { position: relative; white-space: nowrap; }
  .benefit-list li::before {
    content: "\2739"; font-style: normal; font-size: 13px;
    color: var(--white); position: absolute; left: -24px; top: 0;
  }
  .benefit-list li:nth-child(1) { margin-left: 424px; }
  .benefit-list li:nth-child(2) { margin-left: 460px; }
  .benefit-list li:nth-child(3) { margin-left: 496px; }
  .benefit-list li:nth-child(4) { margin-left: 532px; }
  .benefit-list li:nth-child(5) { margin-left: 568px; }
  .testimonial {
    position: absolute; left: 340px; top: 206px; width: 440px;
    text-align: center;
    font-family: "Russo One", "Arial Black", sans-serif;
    font-size: 17px; line-height: 24px;
    color: var(--white);
    letter-spacing: 0.4px;
  }
  .testimonial .accent { color: var(--wanted-yellow); }
</style>
</head>
<body>
<main class="stage">
  <section class="banner" aria-label="Personal empowerment recruitment banner">
    <svg class="banner-shapes" viewBox="0 0 939 262" aria-hidden="true">
      <defs>
        <linearGradient id="left-panel" x1="0" y1="0" x2="0" y2="1">
          <stop offset="0" stop-color="#c95672"/>
          <stop offset="0.45" stop-color="#a83049"/>
          <stop offset="1" stop-color="#5e0411"/>
        </linearGradient>
        <linearGradient id="middle-panel" x1="0" y1="0" x2="1" y2="0.3">
          <stop offset="0" stop-color="#c24f6b"/>
          <stop offset="0.55" stop-color="#a8304c"/>
          <stop offset="1" stop-color="#7d0f26"/>
        </linearGradient>
      </defs>
      <rect x="0" y="0" width="939" height="262" fill="url(#middle-panel)"/>
      <rect x="330" y="200" width="420" height="62" fill="#5a0012"/>
      <path d="M0 0 H330 Q378 130 322 262 H0 Z" fill="url(#left-panel)"/>
      <path d="M330 0 Q378 130 322 262" fill="none" stroke="#ffffff" stroke-width="4"/>
    </svg>
    <div class="photo-slot" role="img" aria-label="Photo of a smiling family of three standing together in a hall"></div>

    <h1 class="headline-wanted">WANTED</h1>
    <p class="headline-call">DRIVEN AND SUCCESSFUL<br>INDIVIDUALS READY TO<br>TAKE THEIR RESULTS TO<br>THE NEXT LEVEL.</p>

    <h2 class="offer-title">Personal Empowerment.</h2>
    <p class="offer-subtitle">The Next Big Business Boom !</p>
    <ul class="benefit-list">
      <li>Make up to $5000 per sale</li>
      <li>No cold calling</li>
      <li>No experience required</li>
      <li>No pressure selling</li>
      <li>NOT MLM</li>
    </ul>

    <p class="testimonial">I MAKE WELL IN EXCESS OF<br><span class="accent">10K</span> PER MONTH CONSISTENTLY. <span class="accent">MARNIE K</span></p>
  </section>
</main>
</body>
</html>
```